Copper Fennel Row Website A Website design for book editing

A website design for book editing

Our proofreading, editing and manuscript review packages are specifically tailored to help you publish the best possible version of your story.

NEED HELP PUBLISHING A BESTSELLER?

If you’re looking for professional book editing services from senior publishing industry insiders, look no further. Besides editing, we can also answer all your publishing questions and get you started building your author platform.

OUR SERVICES

We've carefully structured our packages to maximize value for every budget.

PRICING

$.02
PER WORD
Proofreading
Line Edit (Copy-editing)
Fix spelling and grammar
Sales copy/summary revision

$.04
PER WORD
Proofreading
Line Edit (Copy-editing)
Fix spelling and grammar
Organization and content
Plot and pacing
Manuscript Review

$.06
PER WORD
Proofreading
Line Edit (Copy-editing)
Fix spelling and grammar
Organization and content
Plot and pacing
Manuscript Review
Formatting (print and ebook)
Pre-publication proofread

OUR PROCESS

Send us a sample of your book. Our caffeine-fueled, eagle-eyed editors will go through it and then email you with their comments and suggestions. You can ask them any questions you want. They will look for…

Typos and grammatical errors.
Spelling and word choice issues
Punctuation and style
Word choice, clarity and flow.
Sentence structure and craft
If your writing is already clean, then they’ll discuss bigger picture things with you, like theme, concept, purpose, audience, potential market and branding (including title, subtitle, and tagline or elevator pitch).

Once you feel comfortable and confident in an editor’s expertise, skill and knowledge, and are ready to move ahead, we’ll send an invoice for the first half of the total word count so the editor can get started. We’ll charge the rest when the project is close to completion.

Target Market(s)

Authors

Industry/Entity Type

Book Publisher

Coding

Coded - Design and coding required

Number of Pages Required

1 page

Requirements
Must have
• OUR SERVICES
• We've carefully structured our packages to maximize value for every budget.
• PRICING
• $.02
• PER WORD
• Proofreading
• Line Edit (Copy-editing)
• Fix spelling and grammar
• Sales copy/summary revision
• $.04
• PER WORD
• Proofreading
• Organization and content
• Plot and pacing
• Manuscript Review
• $.06
• PER WORD
• Proofreading
• Plot and pacing
• Manuscript Review
• Formatting (print and ebook)
• Pre-publication proofread

```html
<!DOCTYPE html>
<html lang="en">
<head>
<meta charset="utf-8">
<title>Copper Fennel Row – Book Editing</title>
<link href="https://fonts.googleapis.com/css2?family=Open+Sans:wght@400;600;700&family=Raleway:wght@400;600;700&display=swap" rel="stylesheet">
<style>
:root{
  --red:#e3262d;
  --red-dark:#c81e25;
  --ink:#2e2e2e;
  --muted:#8c8c8c;
  --grey-icon:#8e8e8e;
  --line:#e3e3e3;
  --paper:#ffffff;
  --soft:#f6f6f6;
  --footer:#2c2e33;
  --footer-circle:#3b3e44;
}
*{margin:0;padding:0;box-sizing:border-box}
html,body{width:1200px;height:2416px;overflow:hidden;background:var(--paper)}
body{font-family:"Open Sans",Arial,sans-serif;color:var(--ink);position:relative}

/* Header */
.site-header{position:absolute;top:0;left:0;width:1200px;height:100px;background:var(--paper);display:flex;align-items:center;justify-content:space-between;padding:0 70px 0 56px}
.brand{font-family:"Raleway",Arial,sans-serif;font-weight:700;font-size:32px;color:var(--red);display:flex;align-items:center;gap:12px}
.brand-dot{width:14px;height:14px;border-radius:50%;background:var(--red)}
.main-nav{display:flex;align-items:center;gap:30px;font-size:15px;color:#555}
.main-nav a{color:inherit;text-decoration:none}
.main-nav a.active{color:var(--red);border-bottom:2px solid var(--red);padding-bottom:4px}
.search-btn{width:40px;height:40px;border:2px solid var(--red);border-radius:50%;display:flex;align-items:center;justify-content:center}

/* Hero */
.hero{position:absolute;top:100px;left:0;width:1200px;height:500px}
.hero-photo{position:absolute;inset:0;background:linear-gradient(120deg,#4a4a4a 0%,#8a8480 35%,#c9c3bb 55%,#9a928a 75%,#5c5652 100%)}
.hero-photo::after{content:"";position:absolute;inset:0;background:rgba(0,0,0,.18)}
.hero-label{position:absolute;left:50%;top:184px;transform:translateX(-50%);background:var(--red);color:#fff;font-family:"Raleway",Arial,sans-serif;font-weight:600;font-size:36px;padding:8px 30px}
.hero-tagline{position:absolute;left:50%;top:264px;transform:translateX(-50%);background:rgba(30,30,30,.82);color:#fff;font-size:26px;font-weight:600;padding:12px 30px;white-space:nowrap}

/* Section headings */
.section-title{font-family:"Raleway",Arial,sans-serif;font-weight:400;font-size:52px;color:var(--red);text-align:center}
.section-sub{font-size:14px;color:var(--muted);text-align:center;margin-top:14px}

/* Services */
.services{position:absolute;top:600px;left:0;width:1200px;height:480px;background:var(--soft)}
.services .section-title{margin-top:72px}
.service-list{display:flex;justify-content:center;gap:64px;margin-top:66px}
.service{width:150px;text-align:center}
.service svg{display:block;margin:0 auto}
.service-name{font-size:15px;color:#777;margin-top:16px;line-height:1.4}
.service.active .service-name{color:var(--red)}

/* Pricing */
.pricing{position:absolute;top:1080px;left:0;width:1200px;height:740px;border-top:1px solid var(--line)}
.pricing .section-title{margin-top:60px}
.plans{position:absolute;top:180px;left:180px;width:840px;height:520px}
.plan{position:absolute;background:var(--paper);border:1px solid var(--line);text-align:center}
.plan.standard{left:0;top:20px;width:270px;height:480px}
.plan.premium{left:268px;top:0;width:304px;height:520px;box-shadow:0 4px 18px rgba(0,0,0,.12);z-index:2}
.plan.ultimate{left:570px;top:20px;width:270px;height:480px}
.plan-name{font-size:17px;font-weight:600;color:#444;margin-top:46px;text-transform:uppercase}
.price{width:112px;height:112px;border-radius:50%;background:var(--grey-icon);color:#fff;margin:22px auto 0;display:flex;flex-direction:column;align-items:center;justify-content:center}
.plan.premium .price{background:var(--red)}
.price strong{font-size:30px;font-weight:700;line-height:1}
.price small{font-size:11px;margin-top:6px}
.features{list-style:none;margin:26px 24px 0}
.features li{font-size:14px;color:#666;padding:12px 0;border-bottom:1px solid var(--line)}
.sign-up{display:inline-block;margin-top:28px;background:var(--grey-icon);color:#fff;font-size:15px;font-weight:600;padding:10px 26px}
.plan.premium .sign-up{background:var(--red)}

/* Testimonial */
.testimonial{position:absolute;top:1820px;left:0;width:1200px;height:360px;background:var(--red);color:#fff}
.quote-mark{position:absolute;font-family:Georgia,serif;font-size:42px;opacity:.8}
.quote-text{position:absolute;left:220px;top:100px;width:560px;font-size:15px;line-height:1.7}
.quote-name{position:absolute;left:220px;top:214px;font-weight:700;font-size:15px}
.quote-date{position:absolute;left:220px;top:238px;font-size:13px;opacity:.85}
.portrait{position:absolute;left:818px;top:48px;width:248px;height:248px;border-radius:50%;border:8px solid #fff;background:radial-gradient(circle at 50% 40%,#d9b9a0 0%,#a2785e 55%,#5a3f33 100%)}
.slide-arrow{position:absolute;top:160px}

/* Footer */
.site-footer{position:absolute;top:2180px;left:0;width:1200px;height:236px;background:var(--footer);color:#bbb;text-align:center}
.site-footer .brand{justify-content:center;margin-top:44px;font-size:34px}
.social{display:flex;justify-content:center;gap:20px;margin-top:38px}
.social span{width:52px;height:52px;border-radius:50%;background:var(--footer-circle);display:flex;align-items:center;justify-content:center}
.copyright{font-size:13px;margin-top:30px}
</style>
</head>
<body>

<header class="site-header">
  <div class="brand"><span class="brand-dot"></span>Copper Fennel Row</div>
  <nav class="main-nav">
    <a class="active" href="#">Home</a>
    <a href="#">About Us</a>
    <a href="#">Services</a>
    <a href="#">Pricing</a>
    <a href="#">Contact Us</a>
    <span class="search-btn">
      <svg width="18" height="18" viewBox="0 0 18 18"><circle cx="7.5" cy="7.5" r="5.5" fill="none" stroke="#e3262d" stroke-width="2"/><line x1="11.5" y1="11.5" x2="16" y2="16" stroke="#e3262d" stroke-width="2" stroke-linecap="round"/></svg>
    </span>
  </nav>
</header>

<section class="hero">
  <div class="hero-photo" role="img" aria-label="Editor's hands marking up a stack of manuscript pages beside a laptop"></div>
  <div class="hero-label">Copper Fennel Row</div>
  <div class="hero-tagline">NEED HELP PUBLISHING A BESTSELLER?</div>
</section>

<section class="services">
  <h2 class="section-title">Our Services</h2>
  <p class="section-sub">We've carefully structured our packages to maximize value for every budget.</p>
  <div class="service-list">
    <div class="service active">
      <svg width="110" height="130" viewBox="0 0 110 130"><path d="M55 128 L38 100 A50 50 0 1 1 72 100 Z" fill="#e3262d"/><circle cx="55" cy="55" r="38" fill="#fff"/><text x="55" y="70" text-anchor="middle" font-family="Raleway,Arial,sans-serif" font-weight="700" font-size="40" fill="#e3262d">A</text></svg>
      <div class="service-name">Typos &amp; grammatical errors</div>
    </div>
    <div class="service">
      <svg width="110" height="130" viewBox="0 0 110 130"><path d="M55 128 L38 100 A50 50 0 1 1 72 100 Z" fill="#8e8e8e"/><circle cx="55" cy="55" r="38" fill="#fff"/><path d="M40 70 L66 44 L72 50 L46 76 L38 78 Z" fill="#8e8e8e"/></svg>
      <div class="service-name">Spelling and word choice issues</div>
    </div>
    <div class="service">
      <svg width="110" height="130" viewBox="0 0 110 130"><path d="M55 128 L38 100 A50 50 0 1 1 72 100 Z" fill="#8e8e8e"/><circle cx="55" cy="55" r="38" fill="#fff"/><rect x="49" y="32" width="12" height="30" rx="3" fill="#8e8e8e"/><circle cx="55" cy="74" r="6" fill="#8e8e8e"/></svg>
      <div class="service-name">Punctuation and style</div>
    </div>
    <div class="service">
      <svg width="110" height="130" viewBox="0 0 110 130"><path d="M55 128 L38 100 A50 50 0 1 1 72 100 Z" fill="#8e8e8e"/><circle cx="55" cy="55" r="38" fill="#fff"/><rect x="38" y="38" width="34" height="36" rx="3" fill="none" stroke="#8e8e8e" stroke-width="4"/><line x1="45" y1="50" x2="65" y2="50" stroke="#8e8e8e" stroke-width="3"/><line x1="45" y1="58" x2="65" y2="58" stroke="#8e8e8e" stroke-width="3"/><line x1="45" y1="66" x2="58" y2="66" stroke="#8e8e8e" stroke-width="3"/></svg>
      <div class="service-name">Word choice, clarity and flow</div>
    </div>
    <div class="service">
      <svg width="110" height="130" viewBox="0 0 110 130"><path d="M55 128 L38 100 A50 50 0 1 1 72 100 Z" fill="#8e8e8e"/><circle cx="55" cy="55" r="38" fill="#fff"/><circle cx="55" cy="46" r="10" fill="#8e8e8e"/><path d="M36 76 A19 17 0 0 1 74 76 Z" fill="#8e8e8e"/></svg>
      <div class="service-name">Sentence structure and craft</div>
    </div>
  </div>
</section>

<section class="pricing">
  <h2 class="section-title">Pricing Plan</h2>
  <p class="section-sub">Proofreading, editing and manuscript review packages tailored to help you publish your best story.</p>
  <div class="plans">
    <div class="plan standard">
      <h3 class="plan-name">Standard Plan</h3>
      <div class="price"><strong>$.02</strong><small>PER WORD</small></div>
      <ul class="features">
        <li>Proofreading</li>
        <li>Line Edit (Copy-editing)</li>
        <li>Fix spelling and grammar</li>
        <li>Sales copy/summary revision</li>
      </ul>
      <span class="sign-up">SIGN UP</span>
    </div>
    <div class="plan premium">
      <h3 class="plan-name">Premium Plan</h3>
      <div class="price"><strong>$.04</strong><small>PER WORD</small></div>
      <ul class="features">
        <li>Proofreading</li>
        <li>Line Edit (Copy-editing)</li>
        <li>Fix spelling and grammar</li>
        <li>Organization and content</li>
        <li>Plot and pacing</li>
      </ul>
      <span class="sign-up">SIGN UP</span>
    </div>
    <div class="plan ultimate">
      <h3 class="plan-name">Ultimate Plan</h3>
      <div class="price"><strong>$.06</strong><small>PER WORD</small></div>
      <ul class="features">
        <li>Proofreading</li>
        <li>Plot and pacing</li>
        <li>Manuscript Review</li>
        <li>Formatting (print and ebook)</li>
        <li>Pre-publication proofread</li>
      </ul>
      <span class="sign-up">SIGN UP</span>
    </div>
  </div>
</section>

<section class="testimonial">
  <svg class="slide-arrow" style="left:44px" width="24" height="44" viewBox="0 0 24 44"><polyline points="20,4 4,22 20,40" fill="none" stroke="rgba(255,255,255,.55)" stroke-width="3"/></svg>
  <span class="quote-mark" style="left:196px;top:70px">&ldquo;</span>
  <p class="quote-text">Their editors caught every slip in my manuscript and gave honest notes on plot and pacing. The process was clear, the comments were kind, and my novel reads far better now.</p>
  <span class="quote-mark" style="left:744px;top:140px">&rdquo;</span>
  <div class="quote-name">MARA QUILLBY</div>
  <div class="quote-date">Posted on 07 July 2016</div>
  <div class="portrait" role="img" aria-label="Portrait photo of a satisfied author"></div>
  <svg class="slide-arrow" style="left:1132px" width="24" height="44" viewBox="0 0 24 44"><polyline points="4,4 20,22 4,40" fill="none" stroke="rgba(255,255,255,.55)" stroke-width="3"/></svg>
</section>

<footer class="site-footer">
  <div class="brand"><span class="brand-dot"></span>Copper Fennel Row</div>
  <div class="social">
    <span></span><span></span><span></span><span></span><span></span>
    <span><svg width="20" height="14" viewBox="0 0 20 14"><rect x="1" y="1" width="18" height="12" fill="none" stroke="#bbb" stroke-width="1.6"/><polyline points="1,1 10,8 19,1" fill="none" stroke="#bbb" stroke-width="1.6"/></svg></span>
  </div>
  <p class="copyright">© Copyright 2016 Copper Fennel Row. All Rights Reserved.</p>
</footer>

</body>
</html>
```